Synthex Company Overview

Take our boring and standard word document Company profile and overview and turn into an exciting brochure

Target Market(s)

CFO, CIO, CTO, FM, Directors, Senior Staff at corporate companies, government and private companies

Industry/Entity Type

It Company

Requirements
Must have
• funky
innovative
modern
Nice to have
• Must use synthex Blue

```html
<!DOCTYPE html>
<html lang="en">
<head>
<meta charset="utf-8">
<title>Synthex Company Overview</title>
<link href="https://fonts.googleapis.com/css2?family=Arimo:wght@400;700&display=swap" rel="stylesheet">
<style>
  :root {
    --navy: #14284f;
    --navy-deep: #0c1a38;
    --synthex-blue: #2a8fd0;
    --tag-blue: #3b95cf;
    --ink: #2e2e33;
    --paper: #ffffff;
    --backdrop: #e7e4df;
  }
  * { box-sizing: border-box; margin: 0; padding: 0; }
  html, body { width: 1200px; height: 852px; overflow: hidden; }
  body {
    background: var(--backdrop);
    font-family: "Arimo", Arial, sans-serif;
    color: var(--ink);
    display: flex;
    justify-content: center;
    align-items: center;
    gap: 22px;
  }
  .page {
    width: 370px;
    height: 523px;
    background: var(--paper);
    box-shadow: 0 3px 10px rgba(0,0,0,.18);
    display: flex;
    flex-direction: column;
    overflow: hidden;
  }
  .page-header {
    height: 112px;
    display: flex;
    background: var(--navy);
    flex-shrink: 0;
  }
  .brand-strip {
    width: 96px;
    background: linear-gradient(180deg, #1b3566, var(--navy-deep));
    padding: 30px 0 0 14px;
  }
  .brand-name {
    color: #ffffff;
    font-weight: 700;
    font-size: 12px;
    letter-spacing: .5px;
  }
  .header-visual {
    flex: 1;
    background: radial-gradient(ellipse at 25% 55%, #4aa3e0 0%, #1f5a9e 35%, #152c5a 75%);
  }
  .page-body {
    padding: 26px 30px 20px;
    font-size: 6px;
    line-height: 1.5;
  }
  .page-title {
    color: var(--synthex-blue);
    font-weight: 700;
    font-size: 11px;
    margin-bottom: 9px;
    letter-spacing: .2px;
  }
  .page-body p { margin-bottom: 7px; }
  .overview .page-body { font-size: 5.6px; line-height: 1.42; padding-top: 20px; }
  .overview .page-body p { margin-bottom: 3px; }
  .section-tag {
    display: inline-block;
    background: var(--tag-blue);
    color: #ffffff;
    font-weight: 700;
    font-size: 6px;
    padding: 1px 10px;
    margin: 2px 0 3px;
    letter-spacing: .3px;
  }
</style>
</head>
<body>

<article class="page summary">
  <header class="page-header">
    <div class="brand-strip"><span class="brand-name">SYNTHEX</span></div>
    <div class="header-visual" role="img" aria-label="Hand touching glowing app icons on a blue screen"></div>
  </header>
  <section class="page-body">
    <h1 class="page-title">EXECUTIVE SUMMARY</h1>
    <p>Synthex IT is South Africa’s largest independently owned, national black empowered, ICT network integration and infrastructure management specialist.</p>
    <p>A renowned leader in the field of system integration, infrastructure management, and support services, employing highly skilled professionals.</p>
    <p>Synthex IT is the innovator, founder and operator of the only South African-based Pulse Hub® (www.pulsehub.example), providing a digital hub to manage and regulate many of the country’s leading corporations.</p>
    <p>Synthex IT provides a national support footprint with a single point of contact at our World Class Pulse Hub, where all support calls and third party calls are managed. The Pulse Hub also houses our remote support agents, whom can remotely take control of any workstation or server anywhere on the planet utilising software that allows the end user to control the access.</p>
    <p>The company’s core focus is on Managed ICT Services and Network Infrastructures, specialising in the design, planning, deployment, management, and maintenance. The South African offices are found in Gauteng, Cape Town, Durban, East London and Botswana and it has representation in Port Elizabeth, and across the Southern African region.</p>
    <p>Synthex IT is a Gold Certified Corvex solution provider in 8 competencies. Namely: Advanced Infrastructure Solutions, Unified Communication Solutions, Network Infrastructure Solutions Information Worker Solutions, Mobility Solutions, Security Solutions, Hosting Solutions, OEM Hardware Solutions. Synthex IT also holds the distinction of being one of only a handful of Corvex Premier Partners, which provides them with direct access to Corvex’s highest resources, technical and otherwise in Redmond, Virginia (USA).</p>
    <p>The company has been acknowledged and accredited with many prestigious, local &amp; international, awards, namely: Corvex GOLD Partner of the Year; The Most Innovative ICT Company in Africa; National Business Awards for Entrepreneur of the Year ; National Business Award - Technology Through Innovation; Meridia Bank Entrepreneur of the year Award, CIO of the Year for South Africa; Best Customer Experience of the Year; Networking Infrastructure Solution of the Year; Security Solution of the Year (Middle East, Africa, &amp; Eastern Europe); Global Business Partner of the Year (Worldwide Winner), African ICT Achiever awards – Overall Winner, and many others, every year, since inception.</p>
  </section>
</article>

<article class="page profile">
  <header class="page-header">
    <div class="brand-strip"><span class="brand-name">SYNTHEX</span></div>
    <div class="header-visual" role="img" aria-label="Hand touching glowing app icons on a blue screen"></div>
  </header>
  <section class="page-body">
    <p>Named as one of the country’s Top ICT Companies, and recently winning the Technology Top 100 Company award, Synthex IT has proved and established itself as a strategic partner with numerous internationally-recognised technology vendors and industry leaders.</p>
    <p>Synthex IT prides itself in providing numerous leading, ‘value-added’, ICT Services, and outcome based service level agreements which are measured on the service the client requires, and which ensures the matrix that the client agrees upon. Whereas in the past and with many of our competitors you pay for onsite resources, amount of calls and support hours with us you pay for the agreed result.</p>
    <p>Synthex IT provides outsource ICT services to many large enterprises. Many of our clients are the country’s most prominent and respected companies, as well as a renowned global giant. They are renowned leaders in the Advertising Industry, the Mining Industry, the Telecoms Industry, the Travel Industry, the Financial Industry, and the Retail and Manufacturing Industry.</p>
    <p>Synthex IT also have the distinct privilege of providing our services and working closely with leading companies in South Africa and the largest ICT companies in the world, filling gaps in their offering and outsource requirements and allows them to remain at the cutting edge of their trade.</p>
    <p>Our footprint, size, agility and skills matrix enable them to react quickly and efficiently to changes within the industry and within the world, which they in turn pass onto their clients, assisting them in becoming more productive, efficient and reducing Total Cost of Ownership.</p>
  </section>
</article>

<article class="page overview">
  <header class="page-header">
    <div class="brand-strip"><span class="brand-name">SYNTHEX</span></div>
    <div class="header-visual" role="img" aria-label="Hand touching glowing app icons on a blue screen"></div>
  </header>
  <section class="page-body">
    <h1 class="page-title">COMPANY OVERVIEW</h1>
    <span class="section-tag">MISSION STATEMENT</span>
    <p>Synthex IT aims to be recognised as the preferred ICT Service Partner, focused on innovative, integrated and managed services which add value to all spheres of business operation and give clients genuine peace of mind. In addition, the Synthex brand strives to deliver customer-defined quality service, by attracting, developing and retaining exceptional people and by building strong technology partnerships.</p>
    <span class="section-tag">COMPANY BACKGROUND</span>
    <p>Synthex IT was founded in March 2001 and has been running successfully ever since. Synthex IT now has a national presence with offices in Johannesburg, Cape Town, Durban, East London and representation in Port Elizabeth, Nelspruit, Kimberly, and George. We have also expanded internationally with offices in Botswana and a presence in Namibia. Synthex IT supports and services companies across the globe.</p>
    <p>Synthex IT saw an opportunity to build a world class IT services business leveraging and specialising in Corvex based technology, as well as with other industry technology leaders. Synthex IT has built a reputation as renowned industry leader, not only locally, but internationally as well. Synthex IT is regarded as one of the most accredited and respected Corvex partners in the country. Particularly with regards to the delivery of world class, value-add, IT services and solutions.</p>
    <p>Synthex IT has evolved in to an agile, dynamic, innovative, and leading ICT Company that is renowned in the field of System Integration, Managed IT Services and IT Outsourcing, and is constantly at the forefront of cutting-edge technology, with highly skilled, qualified and best of breed IT personnel.</p>
    <p>Synthex IT is an ICT company focused on Network Infrastructures and the architecture, design, deployment, and support &amp; maintenance thereof, as well as Managed Services (such as off-site back-ups, remote monitoring and support, faxing solutions, spamming solutions, e-mail archiving, business continuity, etc etc). We are one of the few true IT solution focused companies.</p>
    <span class="section-tag">BUSINESS STRATEGY</span>
    <p>Synthex IT has continued to build on its founding strategy of developing a world class Corvex centric business, as well as focusing on other best of breed technologies. Synthex IT has built a world class Pulse Hub that offers remote support, monitoring, and maintenance through a combination of world class integrated technologies. This has contributed towards the company’s organic growth and ongoing success.</p>
    <p>Synthex IT has diversified its capabilities to include Networking and Security services. Beyond this we also identified the coming together of market needs and technology capabilities which lent themselves to the concept of hosted shared services. As a result of this our diversification has refined our core service offering to be based on a hosted shared service capability focusing on, local and global, industry leading technologies. This current service is being further enhanced as the market needs and technology capabilities develop, thereby enabling our growth along the IT maturity curve to a destination of a Utility Based Computing service offering.</p>
    <p>This strategy remains based on our core competency and allows growth in-line with evolving IT and business trends.</p>
  </section>
</article>

</body>
</html>
```